Media Services Start-up -- Corporate Website and Logo Design. Inspiration required!

We need a logo design and corporate website design, including coding, for our start-up business.
Brenvora’s value proposition is based on bringing together media content from a vast number of geographies globally, adding human and AI curation, translation and editing, and delivering the content using tailored customer interfaces. On the one hand, the business brings together media coverage from all over the world, and on the other it brings together content, human skills and technology to deliver a supreme customer experience.
Brenvora is a B2B media monitoring and analytics business with emphasis on global customers. Brenvora's service offering is centred around sourcing media content from different markets, processing, storing and delivering the content and insights derived from it using an online platform / mobile app.
The messaging we want to create through the logo is:
- Global scope
- Speed of delivery
- Cost-efficiency
- Multi-lingual
- Tailor-made
- Trustworthy
Target Market(s)
Business to business, PR / Communications, Media, Marketing
Logo Text
Brenvora
Coding
Coded - Design and coding required
Number of Pages Required
5+ page
Font styles to use
Other font styles liked:
- See Design Brief for details
Colors
Designer to choose colors to be used in the design.

```html
<!DOCTYPE html>
<html lang="en">
<head>
<meta charset="utf-8">
<title>Brenvora — How We Do It</title>
<link href="https://fonts.googleapis.com/css2?family=Questrial&display=swap" rel="stylesheet">
<style>
:root{
  --sky:#66b0ec;
  --card:#6dbfe3;
  --dot:#4cc5f6;
  --orange:#f47322;
  --placeholder:#f0f0f0;
  --ink:#111;
  --text:#444;
  --sand:#f3f0ed;
  --navy:#06132f;
  --footer-head:#1da1e6;
  --white:#fff;
}
*{box-sizing:border-box;margin:0;padding:0}
html,body{width:929px;height:1200px;overflow:hidden;background:var(--white)}
body{font-family:"Questrial",sans-serif;color:var(--text);position:relative}
.hero{position:absolute;left:0;top:0;width:929px;height:230px}
.hero svg{position:absolute;left:0;top:0}
.topbar{position:absolute;top:7px;left:603px;display:flex;align-items:center;gap:11px;color:var(--white);font-size:7.5px}
.cta-small{background:var(--orange);color:#222;border-radius:3px;width:76px;height:19px;display:flex;align-items:center;justify-content:center;gap:3px;font-size:7.5px}
.nav{position:absolute;top:44px;left:0;width:929px;height:12px;color:var(--white);font-size:9px}
.nav span{position:absolute;white-space:nowrap}
.hero-title{position:absolute;top:123px;left:0;width:929px;text-align:center;color:var(--white);font-size:29px;font-weight:400}
.steps{position:absolute;top:246px;left:0;width:929px;height:60px}
.steps .track{position:absolute;top:42px;left:159px;width:611px;height:1px;background:#eaeaea}
.step-num{position:absolute;top:0;width:20px;margin-left:-10px;text-align:center;font-size:9px;color:#333}
.step-dot{position:absolute;top:24px;width:38px;height:38px;margin-left:-19px;border-radius:50%;background:var(--dot);display:flex;align-items:center;justify-content:center}
.card{position:absolute;top:326px;width:287px;height:411px;background:var(--card);padding:19px 19px 0}
.card::before{content:"";position:absolute;top:-8px;left:50%;margin-left:-8px;border-left:8px solid transparent;border-right:8px solid transparent;border-bottom:8px solid var(--card)}
.card-image{width:251px;height:250px;background:var(--placeholder)}
.card h3{font-weight:400;font-size:15px;color:#555;margin-top:9px;line-height:18px}
.card p{font-size:9.8px;line-height:15px;margin-top:8px;color:var(--text)}
.signup{position:absolute;top:807px;left:0;width:929px;height:154px;background:var(--sand)}
.signup h2{position:absolute;top:28px;width:100%;text-align:center;font-weight:400;font-size:35px;color:var(--ink)}
.field{position:absolute;top:78px;width:128px;height:28px;background:var(--white);border:1px solid #999;font-size:9px;color:#888;padding:0 10px;display:flex;align-items:center}
.submit{position:absolute;top:78px;left:609px;width:128px;height:28px;background:var(--orange);color:var(--white);border-radius:2px;font-size:9px;display:flex;align-items:center;justify-content:center;letter-spacing:.2px}
.footer{position:absolute;top:961px;left:0;width:929px;height:239px;background:var(--navy);color:var(--white)}
.col{position:absolute;top:27px;width:220px}
.col h4{font-weight:400;font-size:9px;color:var(--footer-head);text-transform:uppercase;margin-bottom:18px}
.col li{list-style:none;font-size:10px;line-height:14px;margin-bottom:4px;display:flex;align-items:center;gap:3px}
.rule{position:absolute;top:195px;left:132px;width:666px;border-top:1px dotted #3a4766}
.copy{position:absolute;top:208px;width:100%;text-align:center;font-size:8px;font-weight:700}
</style>
</head>
<body>
<header class="hero">
  <svg width="929" height="230" viewBox="0 0 929 230">
    <defs>
      <linearGradient id="heroShade" x1="0" y1="0" x2="1" y2="1">
        <stop offset="0" stop-color="#5b9fd8"/>
        <stop offset=".15" stop-color="#66b0ec"/>
        <stop offset=".85" stop-color="#66b0ec"/>
        <stop offset="1" stop-color="#2a4f78"/>
      </linearGradient>
    </defs>
    <polygon points="0,0 929,0 929,228 0,172" fill="url(#heroShade)"/>
  </svg>
  <div class="topbar">
    <span>Call us on: +(61) 02 5550 1847</span>
    <span class="cta-small">Learn more
      <svg width="7" height="7" viewBox="0 0 10 10"><circle cx="5" cy="5" r="4" fill="none" stroke="#222" stroke-width="1.2"/><path d="M3 5h4M5.5 3.5 7 5 5.5 6.5" fill="none" stroke="#222" stroke-width="1.2"/></svg>
    </span>
  </div>
  <nav class="nav">
    <span style="left:452px">Home</span>
    <span style="left:501px">Solutions</span>
    <span style="left:564px">How We Do It</span>
    <span style="left:647px">Our People</span>
    <span style="left:719px">Our Technology</span>
  </nav>
  <h1 class="hero-title">How we process and deliver solutions</h1>
</header>

<section class="steps">
  <div class="track"></div>
  <span class="step-num" style="left:159px">1</span>
  <span class="step-num" style="left:465px">2</span>
  <span class="step-num" style="left:770px">3</span>
  <div class="step-dot" style="left:159px"><svg width="16" height="16" viewBox="0 0 16 16"><circle cx="8" cy="8" r="7" fill="var(--white)"/><path d="M4 5c2-1 3 0 3 2s-2 1-2 3M10 4c1 2 3 2 3 4s-2 3-3 4" fill="none" stroke="var(--dot)" stroke-width="1.4"/></svg></div>
  <div class="step-dot" style="left:465px"><svg width="16" height="16" viewBox="0 0 16 16"><circle cx="8" cy="8" r="7" fill="var(--white)"/><path d="M4 5c2-1 3 0 3 2s-2 1-2 3M10 4c1 2 3 2 3 4s-2 3-3 4" fill="none" stroke="var(--dot)" stroke-width="1.4"/></svg></div>
  <div class="step-dot" style="left:770px"><svg width="20" height="20" viewBox="0 0 20 20"><rect x="1" y="1" width="18" height="18" rx="2" fill="var(--white)"/></svg></div>
</section>

<article class="card" style="left:15px">
  <div class="card-image" role="img" aria-label="Photo illustrating step one of the process"></div>
  <h3>How we do it #1</h3>
  <p>Lorem ipsum dolor sit amet, mea ei viderer probatus consequuntur, sonet vocibus lobortis has ad. Eos erant indoctum an, dictas invidunt est ex, et sea consulatu torquatos. Nostro aperiam petentium eu nam, mel debet urbanitas ad, idque complectitur eu quo. An sea autem dolore dolores.</p>
</article>
<article class="card" style="left:321px">
  <div class="card-image" role="img" aria-label="Photo illustrating step two of the process"></div>
  <h3>How we do it #2</h3>
  <p>Lorem ipsum dolor sit amet, mea ei viderer probatus consequuntur, sonet vocibus lobortis has ad. Eos erant indoctum an, dictas invidunt est ex, et sea consulatu torquatos. Nostro aperiam petentium eu nam, mel debet urbanitas ad, idque complectitur eu quo. An sea autem dolore dolores.</p>
</article>
<article class="card" style="left:627px">
  <div class="card-image" role="img" aria-label="Photo illustrating step three of the process"></div>
  <h3>How we do it #3</h3>
  <p>Lorem ipsum dolor sit amet, mea ei viderer probatus consequuntur, sonet vocibus lobortis has ad. Eos erant indoctum an, dictas invidunt est ex, et sea consulatu torquatos. Nostro aperiam petentium eu nam, mel debet urbanitas ad, idque complectitur eu quo. An sea autem dolore dolores.</p>
</article>

<section class="signup">
  <h2>Learn more about Brenvora</h2>
  <div class="field" style="left:192px">Name</div>
  <div class="field" style="left:331px">Email</div>
  <div class="field" style="left:470px">Phone</div>
  <div class="submit">GET STARTED</div>
</section>

<footer class="footer">
  <div class="col" style="left:132px">
    <h4>Brenvora</h4>
    <ul>
      <li><svg width="6" height="9" viewBox="0 0 6 9"><path d="M3 0a3 3 0 0 0-3 3c0 2 3 6 3 6s3-4 3-6a3 3 0 0 0-3-3z" fill="var(--white)"/><circle cx="3" cy="3" r="1.1" fill="var(--navy)"/></svg>48 Harbour Lane, Portland, OR 97204.</li>
      <li><svg width="8" height="8" viewBox="0 0 10 10"><path d="M2 0l2 2-1 2c1 1 2 2 3 3l2-1 2 2-2 2C4 10 0 6 0 2z" fill="var(--white)"/></svg>555.019283</li>
      <li><svg width="10" height="8" viewBox="0 0 10 8"><rect x=".5" y=".5" width="9" height="7" fill="none" stroke="var(--white)"/><path d="M.5 .5 5 4.5 9.5 .5" fill="none" stroke="var(--white)"/></svg>info@brenvora.com</li>
    </ul>
  </div>
  <div class="col" style="left:362px">
    <h4>Solutions</h4>
    <ul>
      <li>Content Sourcing</li>
      <li>Content Collection</li>
      <li>Content Augmentation</li>
      <li>Content Delivery</li>
      <li>Media Insights &amp; Consultancy</li>
    </ul>
  </div>
  <div class="col" style="left:592px;width:190px">
    <h4>Our Technology</h4>
    <ul>
      <li>Content Ingestion / Normalisation &amp; Augmentation</li>
      <li>Content Delivery</li>
      <li>Insight Services</li>
    </ul>
  </div>
  <div class="rule"></div>
  <div class="copy">© 2019 Brenvora</div>
</footer>
</body>
</html>
```